Corwell Facilities Services Business Card.

We need a card for Corwell Facilities Services with a new look. We also have service and supply partners that we would like to have on the card. Glazomark is a surface application company, Corwell Facilities is a facilities services business, Tavish Supply Co is a Facilities supply business, Plevra is a product that we use that powers our business.

```html
<!DOCTYPE html>
<html lang="en">
<head>
<meta charset="utf-8">
<title>Corwell Facilities Services – Business Card</title>
<link href="https://fonts.googleapis.com/css2?family=Nunito:wght@700;800&family=Roboto:wght@400;500&display=swap" rel="stylesheet">
<style>
  :root {
    --page-bg: #dcd7cf;
    --card-bg: #eef0f0;
    --card-edge: #c9ccce;
    --brand-blue: #2d5a96;
    --brand-green: #1f8a4c;
    --ink: #2f2f2f;
    --ink-soft: #3c3c3c;
    --ink-muted: #6a6f74;
    --mark-faint: rgba(45, 90, 150, 0.07);
  }
  * { margin: 0; padding: 0; box-sizing: border-box; }
  html, body {
    width: 1200px;
    height: 1054px;
    overflow: hidden;
    background: var(--page-bg);
  }
  .card {
    position: absolute;
    left: 100px;
    top: 225px;
    width: 1000px;
    height: 604px;
    background: var(--card-bg);
    border: 1px solid var(--card-edge);
    overflow: hidden;
    font-family: "Roboto", Arial, sans-serif;
  }
  .side-band {
    position: absolute;
    left: 0; top: 0;
    width: 89px; height: 100%;
    background: linear-gradient(to bottom, var(--brand-blue) 0%, #2c6a86 45%, var(--brand-green) 100%);
  }
  .side-rule {
    position: absolute;
    left: 97px; top: 0;
    width: 5px; height: 100%;
    background: linear-gradient(to bottom, var(--brand-green) 0%, var(--brand-green) 45%, var(--brand-blue) 100%);
  }
  .faint-mark {
    position: absolute;
    left: 660px; top: 110px;
    width: 290px; height: 290px;
    border-radius: 50%;
    background: var(--mark-faint);
  }
  .brand {
    position: absolute;
    left: 150px; top: 50px;
    display: flex;
    align-items: center;
    gap: 18px;
  }
  .brand-dot {
    width: 92px; height: 92px;
    border-radius: 50%;
    background: var(--brand-blue);
    flex: none;
  }
  .brand-name {
    font-family: "Nunito", Arial, sans-serif;
    font-weight: 800;
    color: var(--brand-blue);
    line-height: 1;
  }
  .brand-name .brand-lead {
    display: block;
    font-size: 84px;
    letter-spacing: -1px;
  }
  .brand-name .brand-rest {
    display: block;
    font-size: 33px;
    margin-top: 2px;
  }
  .person-name {
    position: absolute;
    left: 149px; top: 292px;
    font-family: "Nunito", Arial, sans-serif;
    font-weight: 700;
    font-size: 37px;
    color: var(--brand-blue);
  }
  .person-title {
    position: absolute;
    left: 149px; top: 340px;
    font-size: 23px;
    color: var(--ink-soft);
  }
  .contact-list {
    position: absolute;
    left: 149px; top: 412px;
    list-style: none;
  }
  .contact-list li {
    display: flex;
    align-items: center;
    height: 38px;
    font-size: 23px;
    color: var(--ink);
  }
  .contact-list svg {
    width: 22px; height: 22px;
    margin-right: 29px;
    fill: var(--brand-blue);
  }
  .address {
    position: absolute;
    left: 149px; top: 531px;
    font-size: 23px;
    color: var(--ink);
  }
  .partners {
    position: absolute;
    right: 44px; top: 420px;
    text-align: right;
  }
  .partners-label {
    font-size: 13px;
    font-weight: 500;
    letter-spacing: 1.5px;
    text-transform: uppercase;
    color: var(--ink-muted);
    margin-bottom: 8px;
  }
  .partners-list {
    list-style: none;
  }
  .partners-list li {
    font-size: 19px;
    line-height: 26px;
    font-weight: 500;
    color: var(--brand-blue);
  }
</style>
</head>
<body>
  <div class="card">
    <div class="side-band"></div>
    <div class="side-rule"></div>
    <div class="faint-mark"></div>

    <div class="brand">
      <div class="brand-dot"></div>
      <div class="brand-name">
        <span class="brand-lead">Corwell</span>
        <span class="brand-rest">Facilities Services</span>
      </div>
    </div>

    <div class="person-name">Maren T. Ellison</div>
    <div class="person-title">Managing Director</div>

    <ul class="contact-list">
      <li>
        <svg viewBox="0 0 24 24" aria-hidden="true"><path d="M3 8c0-2 2-3 9-3s9 1 9 3v2h-5V8H8v2H3zM6 12l3-3h6l3 3v7H6zm6 1.5a2.5 2.5 0 1 0 0 5 2.5 2.5 0 0 0 0-5z"/></svg>
        828-555-0142
      </li>
      <li>
        <svg viewBox="0 0 24 24" aria-hidden="true"><path d="M2 5h20v14H2zm2 2v.5l8 5.5 8-5.5V7zm0 3v7h16v-7l-8 5.5z"/></svg>
        maren@corwellfs.com
      </li>
      <li>
        <svg viewBox="0 0 24 24" aria-hidden="true"><path d="M12 2a10 10 0 1 0 0 20 10 10 0 0 0 0-20zm6.9 9h-3a15 15 0 0 0-1.3-6.1A8 8 0 0 1 18.9 11zM12 4.2c.9 1.3 1.7 3.7 1.9 6.8h-3.8c.2-3.1 1-5.5 1.9-6.8zM9.4 4.9A15 15 0 0 0 8.1 11h-3a8 8 0 0 1 4.3-6.1zM5.1 13h3a15 15 0 0 0 1.3 6.1A8 8 0 0 1 5.1 13zm6.9 6.8c-.9-1.3-1.7-3.7-1.9-6.8h3.8c-.2 3.1-1 5.5-1.9 6.8zm2.6-.7a15 15 0 0 0 1.3-6.1h3a8 8 0 0 1-4.3 6.1z"/></svg>
        www.corwellfs.com
      </li>
    </ul>

    <div class="address">418 Larkspur Ave., Bellhaven, California, US 95731</div>

    <div class="partners">
      <div class="partners-label">Service &amp; Supply Partners</div>
      <ul class="partners-list">
        <li>Glazomark</li>
        <li>Tavish Supply Co</li>
        <li>Plevra</li>
      </ul>
    </div>
  </div>
</body>
</html>
```